Life Coach for Lawyers Business Card Design

Elegant, original, business card design for life coaching service for associate attorneys who work in big law and struggle with stress, overwhelm, and time management. Double sided design.

Target Market(s)

Women associate attorneys who work in big law and struggle with stress, overwhelm, and time management.

Industry/Entity Type

Life Coaching

Contact Information for Business Card

Marissa Pendrell
Life Coach
518.677.3941
calmbriefcounsel.net
marissa@calmbriefcounsel.net
@calmbriefcounsel (Instagram)

Font styles to use
Other font styles liked:
• Silver South font duo. See uploaded files.

Requirements
Must have
• Icons for phone, website, email, and Instagram instead of words. Specific colors used in my logo (171B2B, 421121, FFFFFF)
Nice to have
• Foil. Embossed. Feminine design.
Should not have
• Any colors other than those used in logo. See uploaded files.

```html
<!DOCTYPE html>
<html lang="en">
<head>
<meta charset="utf-8">
<title>Calm Brief Counsel — Business Card</title>
<link rel="stylesheet" href="https://fonts.googleapis.com/css2?family=Bodoni+Moda:wght@400&family=Questrial&display=swap">
<style>
  :root {
    --bg: #b3a1a6;
    --burgundy: #421121;
    --navy: #171b2b;
    --white: #ffffff;
    --silver: #d6d6d8;
  }
  * { margin: 0; padding: 0; box-sizing: border-box; }
  html, body {
    width: 1200px;
    height: 1000px;
    overflow: hidden;
    background: var(--bg);
  }
  .canvas {
    position: relative;
    width: 1200px;
    height: 1000px;
  }
  .card {
    position: absolute;
    width: 660px;
    height: 380px;
  }
  .card--back {
    left: 140px;
    top: 150px;
    background: var(--burgundy);
    display: flex;
    align-items: center;
    justify-content: center;
  }
  .brand-name {
    font-family: "Bodoni Moda", serif;
    font-weight: 400;
    font-size: 40px;
    letter-spacing: 3px;
    text-transform: uppercase;
    color: var(--silver);
    text-align: center;
    line-height: 1.15;
  }
  .card--front {
    left: 430px;
    top: 440px;
    background: var(--white);
    padding: 52px 60px 0 60px;
  }
  .holder-name {
    font-family: "Bodoni Moda", serif;
    font-weight: 400;
    font-size: 38px;
    letter-spacing: 2px;
    text-transform: uppercase;
    color: var(--navy);
    line-height: 1.05;
  }
  .holder-role {
    font-family: "Bodoni Moda", serif;
    font-weight: 400;
    font-size: 25px;
    letter-spacing: 2px;
    text-transform: uppercase;
    color: var(--navy);
    margin-top: 4px;
  }
  .divider {
    display: block;
    margin-top: 14px;
  }
  .contact-list {
    list-style: none;
    margin-top: 50px;
  }
  .contact-item {
    display: flex;
    align-items: center;
    gap: 14px;
    height: 36px;
    font-family: "Questrial", sans-serif;
    font-size: 20px;
    color: var(--burgundy);
  }
  .contact-item:first-child { font-size: 23px; }
  .contact-icon {
    width: 22px;
    height: 22px;
    fill: var(--burgundy);
    flex: none;
  }
</style>
</head>
<body>
<main class="canvas">
  <section class="card card--back" aria-label="Card back">
    <p class="brand-name">Calm Brief<br>Counsel</p>
  </section>

  <section class="card card--front" aria-label="Card front">
    <h1 class="holder-name">Marissa Pendrell</h1>
    <p class="holder-role">Life Coach</p>
    <svg class="divider" width="545" height="16" viewBox="0 0 545 16" aria-hidden="true">
      <line x1="0" y1="13" x2="275" y2="13" stroke="#171b2b" stroke-width="2"/>
      <line x1="275" y1="4" x2="545" y2="4" stroke="#421121" stroke-width="2"/>
    </svg>
    <ul class="contact-list">
      <li class="contact-item">
        <svg class="contact-icon" viewBox="0 0 24 24" aria-hidden="true"><path d="M6.6 10.8a15.1 15.1 0 0 0 6.6 6.6l2.2-2.2a1 1 0 0 1 1-.25 11.4 11.4 0 0 0 3.6.57 1 1 0 0 1 1 1V20a1 1 0 0 1-1 1A17 17 0 0 1 3 4a1 1 0 0 1 1-1h3.5a1 1 0 0 1 1 1c0 1.25.2 2.45.57 3.57a1 1 0 0 1-.25 1z"/></svg>
        <span>518.677.3941</span>
      </li>
      <li class="contact-item">
        <svg class="contact-icon" viewBox="0 0 24 24" aria-hidden="true"><path d="M2 5h20v14H2z M3.5 6.5v.4l8.5 6 8.5-6v-.4z" fill-rule="evenodd"/><path d="M3.5 8.6v8.9h17V8.6L12 14.6z" fill="#ffffff" opacity="0"/></svg>
        <span>marissa@calmbriefcounsel.net</span>
      </li>
      <li class="contact-item">
        <svg class="contact-icon" viewBox="0 0 24 24" aria-hidden="true"><path d="M12 2a10 10 0 1 0 0 20 10 10 0 0 0 0-20zm6.9 6h-2.9a15.6 15.6 0 0 0-1.4-3.6A8 8 0 0 1 18.9 8zM12 4c.8 1.2 1.5 2.5 1.9 4h-3.8c.4-1.5 1.1-2.8 1.9-4zM4.3 14a8 8 0 0 1 0-4h3.4a16.5 16.5 0 0 0 0 4zm.8 2h2.9c.3 1.3.8 2.5 1.4 3.6A8 8 0 0 1 5.1 16zM8 8H5.1a8 8 0 0 1 4.3-3.6C8.8 5.5 8.3 6.7 8 8zm4 12c-.8-1.2-1.5-2.5-1.9-4h3.8c-.4 1.5-1.1 2.8-1.9 4zm2.3-6H9.7a14.7 14.7 0 0 1 0-4h4.6a14.7 14.7 0 0 1 0 4zm.3 5.6c.6-1.1 1.1-2.3 1.4-3.6h2.9a8 8 0 0 1-4.3 3.6zm1.7-5.6a16.5 16.5 0 0 0 0-4h3.4a8 8 0 0 1 0 4z"/></svg>
        <span>calmbriefcounsel.net</span>
      </li>
    </ul>
  </section>
</main>
</body>
</html>
```